Studying Effectively To Do List

I am looking to design a new "Study To Do List" for High School students (Ages 15 - 18) . This will be printed as an A4 notepad and so should only be a single A4 page.

The Design will need to be professional and look semi-serious but also be appealing to High school students (Ages 15 - 18) and should NOT be gender specific.

I have attached a word document outlining the structure of the page. The space provided should be large enough that people can write in it comfortably.

The notepad will most likely be printed in black and white but I'm also looking at coloured options - colours should be kept to a minimum.

This will be printed professionally and should also include a 3mm bleed.

The design should also include the business logo (included in the word document)

Target Market(s)

High School students (Ages 15 - 18). Both genders

Industry/Entity Type

Education

Font styles to use
Serif
Sans Serif

Requirements
Must have
• Please see the word document attached.
Should not have
• Too much colour

```html
<!DOCTYPE html>
<html lang="en">
<head>
<meta charset="utf-8">
<title>To-Do Planner</title>
<link href="https://fonts.googleapis.com/css2?family=Montserrat:wght@300;800&family=Arimo:wght@400;700&display=swap" rel="stylesheet">
<style>
:root{
  --green:#8cc29a;
  --green-light:#c9e7cd;
  --orange:#f47b20;
  --blue:#27a9e1;
  --navy:#263b55;
  --grey:#e6e7e8;
  --line:#d1d3d4;
  --text:#555759;
  --white:#ffffff;
}
*{box-sizing:border-box;margin:0;padding:0}
html,body{width:849px;height:1200px;overflow:hidden;background:var(--white)}
body{position:relative;font-family:"Arimo",Arial,sans-serif;color:var(--text)}
.abs{position:absolute}

.brand{left:120px;top:72px;width:130px;display:flex;flex-direction:column;align-items:center;gap:8px}
.brand-dot{width:44px;height:44px;border-radius:50%;background:var(--navy)}
.brand-name{font-family:"Montserrat",sans-serif;font-weight:800;font-size:15px;color:var(--navy);text-align:center;line-height:1.1}

.divider{left:256px;top:38px;height:1122px;border-left:1px dashed #a7a9ac}

.title-todo{left:287px;top:28px;font-family:"Montserrat",sans-serif;font-weight:800;font-size:56px;line-height:1;color:var(--orange);letter-spacing:1px}
.title-planner{left:287px;top:82px;font-family:"Montserrat",sans-serif;font-weight:300;font-size:50px;line-height:1;color:var(--orange);letter-spacing:1px}
.date{left:644px;top:113px;font-size:12px;width:130px}
.date span{position:absolute;top:0}

.band{height:22px;display:flex;align-items:center;font-weight:700;font-size:15px;color:var(--white);letter-spacing:1.5px}
.band-left{justify-content:flex-end;padding-right:14px;left:40px;width:217px;clip-path:polygon(0 0,100% 0,100% 100%,0 100%,11px 50%)}
.band-right{left:257px;width:552px;padding-left:30px;background:var(--green-light);clip-path:polygon(0 0,100% 0,calc(100% - 11px) 50%,100% 100%,0 100%)}
.band-green{background:var(--green)}
.band-orange{background:var(--orange)}
.band-left svg{margin-right:8px}

.day{left:67px;width:164px;height:51px;border-right:3px solid var(--grey);border-bottom:3px solid var(--grey);text-align:right;font-size:10px;padding:3px 6px 0 0}
.day.weekend{border-color:var(--blue);color:var(--blue)}

.note-line{left:67px;width:160px;border-top:1px solid var(--grey)}

.subject{left:67px;width:160px;font-size:10px;height:20px;display:flex;align-items:flex-end}
.subject i{flex:1;margin-left:12px;border-bottom:1px solid var(--grey);height:100%}

.row{left:288px;width:470px;height:25px;font-size:10px;display:flex;align-items:center;padding-left:16px}
.row.open{border:1px solid var(--grey);background:var(--white)}
.row.shade{background:var(--grey)}
.check{left:771px;width:12px;height:12px;border:1px solid var(--line)}

.assign-head{left:288px;width:470px;height:24px;border:1px solid var(--grey);font-size:10px;display:flex;align-items:center;padding-left:16px}
.due{position:absolute;left:344px;top:6px}
.due span{position:absolute;top:0}
.assign-body{left:288px;width:470px;height:51px;background:var(--grey)}
.assign-body::after{content:"";position:absolute;left:16px;right:16px;top:25px;border-top:1px dashed #bcbec0}
</style>
</head>
<body>

<div class="abs brand">
  <div class="brand-dot"></div>
  <div class="brand-name">Kestrel Prep</div>
</div>

<div class="abs divider"></div>

<div class="abs title-todo">TO-DO</div>
<div class="abs title-planner">PLANNER</div>
<div class="abs date">Date:<span style="left:81px">/</span><span style="left:126px">/</span></div>

<!-- Schedule -->
<div class="abs band band-left band-green" style="top:155px">
  <svg width="11" height="11" viewBox="0 0 11 11"><rect x="0.5" y="1.5" width="10" height="9" fill="none" stroke="#fff"/><rect x="0.5" y="1.5" width="10" height="2.5" fill="#fff"/><rect x="2" y="5.5" width="2" height="1.5" fill="#fff"/><rect x="4.5" y="5.5" width="2" height="1.5" fill="#fff"/><rect x="7" y="5.5" width="2" height="1.5" fill="#fff"/><rect x="2" y="8" width="2" height="1.5" fill="#fff"/><rect x="4.5" y="8" width="2" height="1.5" fill="#fff"/></svg>SCHEDULE
</div>
<div class="abs band band-right" style="top:155px">REVISION TASKS</div>

<div class="abs day" style="top:197px">Monday</div>
<div class="abs day" style="top:254px">Tuesday</div>
<div class="abs day" style="top:311px">Wednesday</div>
<div class="abs day" style="top:368px">Thursday</div>
<div class="abs day" style="top:425px">Friday</div>
<div class="abs day weekend" style="top:482px">Saturday</div>
<div class="abs day weekend" style="top:539px">Sunday</div>

<!-- Revision tasks -->
<div class="abs row open" style="top:198px">01</div>
<div class="abs row shade" style="top:226px">02</div>
<div class="abs row open" style="top:255px">03</div>
<div class="abs row shade" style="top:283px">04</div>
<div class="abs row open" style="top:312px">05</div>
<div class="abs row shade" style="top:340px">06</div>
<div class="abs check" style="top:211px"></div>
<div class="abs check" style="top:239px"></div>
<div class="abs check" style="top:268px"></div>
<div class="abs check" style="top:296px"></div>
<div class="abs check" style="top:325px"></div>
<div class="abs check" style="top:353px"></div>

<!-- Notes -->
<div class="abs band band-left band-orange" style="top:615px">NOTES</div>
<div class="abs note-line" style="top:678px"></div>
<div class="abs note-line" style="top:702px"></div>
<div class="abs note-line" style="top:726px"></div>
<div class="abs note-line" style="top:750px"></div>
<div class="abs note-line" style="top:774px"></div>
<div class="abs note-line" style="top:798px"></div>
<div class="abs note-line" style="top:822px"></div>
<div class="abs note-line" style="top:846px"></div>
<div class="abs note-line" style="top:870px"></div>
<div class="abs note-line" style="top:894px"></div>
<div class="abs note-line" style="top:916px"></div>

<!-- Assignments -->
<div class="abs band band-right" style="top:390px">ASSIGNMENTS</div>

<div class="abs assign-head" style="top:437px">01<div class="due">Due:<span style="left:53px">/</span><span style="left:83px">/</span></div></div>
<div class="abs assign-body" style="top:463px"></div>
<div class="abs assign-head" style="top:518px">02<div class="due">Due:<span style="left:53px">/</span><span style="left:83px">/</span></div></div>
<div class="abs assign-body" style="top:544px"></div>
<div class="abs assign-head" style="top:599px">03<div class="due">Due:<span style="left:53px">/</span><span style="left:83px">/</span></div></div>
<div class="abs assign-body" style="top:625px"></div>
<div class="abs assign-head" style="top:680px">04<div class="due">Due:<span style="left:53px">/</span><span style="left:83px">/</span></div></div>
<div class="abs assign-body" style="top:706px"></div>
<div class="abs assign-head" style="top:761px">05<div class="due">Due:<span style="left:53px">/</span><span style="left:83px">/</span></div></div>
<div class="abs assign-body" style="top:787px"></div>
<div class="abs assign-head" style="top:842px">06<div class="due">Due:<span style="left:53px">/</span><span style="left:83px">/</span></div></div>
<div class="abs assign-body" style="top:868px"></div>
<div class="abs check" style="top:448px"></div>
<div class="abs check" style="top:529px"></div>
<div class="abs check" style="top:610px"></div>
<div class="abs check" style="top:691px"></div>
<div class="abs check" style="top:772px"></div>
<div class="abs check" style="top:853px"></div>

<!-- Homework -->
<div class="abs band band-left band-green" style="top:945px">HOMEWORK</div>
<div class="abs subject" style="top:993px">Subject:<i></i></div>
<div class="abs subject" style="top:1021px">Subject:<i></i></div>
<div class="abs subject" style="top:1050px">Subject:<i></i></div>
<div class="abs subject" style="top:1078px">Subject:<i></i></div>
<div class="abs subject" style="top:1107px">Subject:<i></i></div>
<div class="abs subject" style="top:1135px">Subject:<i></i></div>

<svg class="abs" style="left:244px;top:1066px" width="28" height="18" viewBox="0 0 28 18" aria-label="Arrow pointing to task description">
  <path d="M2 9H24M17 3l7 6-7 6" fill="none" stroke="var(--green)" stroke-width="2"/>
</svg>

<!-- Task description -->
<div class="abs band band-right" style="top:945px">TASK DESCRIPTION</div>
<div class="abs row open" style="top:992px"></div>
<div class="abs row shade" style="top:1020px"></div>
<div class="abs row open" style="top:1049px"></div>
<div class="abs row shade" style="top:1077px"></div>
<div class="abs row open" style="top:1106px"></div>
<div class="abs row shade" style="top:1134px"></div>
<div class="abs check" style="top:1005px"></div>
<div class="abs check" style="top:1033px"></div>
<div class="abs check" style="top:1062px"></div>
<div class="abs check" style="top:1090px"></div>
<div class="abs check" style="top:1119px"></div>
<div class="abs check" style="top:1147px"></div>

</body>
</html>
```